Bref créative
Brookhaven Smile Design (Dentist)
Business cards, stationary, etc.
Professional
*please leave blank as name is in the logo.
842 W. Tamsworth Rd. Suite 5B
Hollisford, NJ 07190
info@BrookhavenSmileDesign.example
BrookhavenSmileDesign.example
We would like the following items included in our package:
1. business cards with rounded edges (3.5X2) with three back choices listed below.
2. One business card with straight edges (3.5x4) which is perforated and can be split into 2 business cards, see uploaded template for ideas.
3. Please include stationary, fax paper, email signature, envelopes.
Four back options that we want:
1) appointment reminder on back (at the bottom of the card I want it to read: *Please note that we require at least 24 hours notice for changed appointments. This time is reserved especially for you. Thank you!
2) simple back with logo and website
3) 3rd back with uploaded image of Free teeth whitening (Please replace 'Free teeth whitening' from uploaded image with 'Free Take-Home Whitening System').
4)On the 3.5x4 business card, the back of one side will be the appointment reminder and the back of the second one will be the uploaded image of the new patient special (Please replace 'free teeth whitening' with: Free Take-Home Whitening System)
The fonts of the logo
Scanned items #3 and #4 are the front and backs of the perforated business cards that are folded. #4 is the outsides of the two folded business cards and #3 is the inside.

```html
<!DOCTYPE html>
<html lang="en">
<head>
<meta charset="utf-8">
<title>Brookhaven Smile Design – Business Card</title>
<link rel="stylesheet" href="https://fonts.googleapis.com/css2?family=Arimo:wght@400;700&display=swap">
<style>
  :root {
    --bg: #e9e6e2;
    --card: #ffffff;
    --blue-deep: #1b5fae;
    --blue-mid: #2f7fd0;
    --blue-light: #6fb2ea;
    --green: #2e9a3f;
    --text: #3a3a3a;
    --rule: #b9bcc0;
  }
  * { margin: 0; padding: 0; box-sizing: border-box; }
  html, body {
    width: 1200px; height: 780px; overflow: hidden;
    background: var(--bg);
    font-family: "Arimo", Arial, sans-serif;
  }
  .canvas { position: relative; width: 1200px; height: 780px; }
  .business-card {
    position: absolute; left: 100px; top: 104px;
    width: 1000px; height: 571px;
    background: var(--card);
    border-radius: 42px;
    overflow: hidden;
    box-shadow: 0 10px 30px rgba(0,0,0,.18);
  }
  .header-band { position: absolute; left: 0; top: 0; width: 1000px; height: 240px; }
  .practice-name {
    position: absolute; left: 0; top: 250px; width: 1000px;
    text-align: center;
    font-size: 40px; font-weight: 700; letter-spacing: 0;
    color: var(--blue-deep); white-space: nowrap;
  }
  .doctor-block {
    position: absolute; left: 0; top: 322px; width: 1000px;
    color: var(--blue-deep); text-align: center; white-space: nowrap;
  }
  .doctor-name { font-size: 24px; letter-spacing: 6px; text-transform: uppercase; }
  .specialty { margin-top: 8px; font-size: 14px; font-weight: 700; letter-spacing: 3px; text-transform: uppercase; }
  .address {
    position: absolute; right: 560px; top: 440px;
    text-align: right; font-size: 19px; line-height: 27px; color: var(--text);
    font-style: normal; white-space: nowrap;
  }
  .divider { position: absolute; left: 462px; top: 432px; width: 1px; height: 92px; background: var(--rule); }
  .contact-list { position: absolute; left: 482px; top: 436px; list-style: none; }
  .contact-list li {
    display: flex; align-items: center; gap: 10px;
    font-size: 18px; line-height: 28px; color: var(--text); white-space: nowrap;
  }
  .contact-icon { width: 20px; height: 20px; flex: none; }
</style>
</head>
<body>
<div class="canvas">
  <div class="business-card">
    <svg class="header-band" viewBox="0 0 1000 240" aria-hidden="true">
      <defs>
        <linearGradient id="bandBlue" x1="0" y1="0" x2="1" y2="0.4">
          <stop offset="0" stop-color="#1b5fae"/>
          <stop offset="0.55" stop-color="#2f7fd0"/>
          <stop offset="1" stop-color="#6fb2ea"/>
        </linearGradient>
      </defs>
      <path d="M0 0 H1000 V95 C780 110 420 150 0 178 Z" fill="url(#bandBlue)"/>
      <path d="M0 190 C420 162 780 124 1000 108 V118 C780 134 420 172 0 200 Z" fill="#2e9a3f"/>
      <path d="M0 206 C420 178 780 140 1000 124 V128 C780 144 420 182 0 210 Z" fill="#1b5fae" opacity=".85"/>
    </svg>

    <div class="practice-name">Brookhaven Smile Design</div>

    <div class="doctor-block">
      <div class="doctor-name">Daniel Marren DMD</div>
      <div class="specialty">Cosmetic &amp; Family Dentistry</div>
    </div>

    <address class="address">
      842 W. Tamsworth Rd.<br>
      Suite 5B, Hollisford,<br>
      NJ 07190
    </address>

    <div class="divider"></div>

    <ul class="contact-list">
      <li>
        <svg class="contact-icon" viewBox="0 0 20 20" aria-hidden="true"><path d="M5 2h4l1 4-2 1.5c1 2 2.5 3.5 4.5 4.5L14 10l4 1v4c0 1-1 2-2 2C9 17 3 11 3 4c0-1 1-2 2-2z" fill="#2f7fd0"/></svg>
        555-014-2783
      </li>
      <li>
        <svg class="contact-icon" viewBox="0 0 20 20" aria-hidden="true"><circle cx="10" cy="10" r="3.5" fill="none" stroke="#2f7fd0" stroke-width="2"/><path d="M13.5 7v4.5c0 1.5 3 1.5 3-1.5A6.5 6.5 0 1 0 13 15.5" fill="none" stroke="#2f7fd0" stroke-width="2"/></svg>
        info@BrookhavenSmileDesign.example
      </li>
      <li>
        <svg class="contact-icon" viewBox="0 0 20 20" aria-hidden="true"><circle cx="10" cy="10" r="8" fill="#2f7fd0"/><path d="M2 10h16M10 2c-3 3-3 13 0 16M10 2c3 3 3 13 0 16" fill="none" stroke="#fff" stroke-width="1.2"/></svg>
        www.BrookhavenSmileDesign.example
      </li>
    </ul>
  </div>
</div>
</body>
</html>
```